Postcard Design

I am attempting to put together a post card that meats the QRX requirements for there mail pay zip code mail program. They are tell different requirements depending on who you talk too. Allied Parcel office, hhhmmmm shock.
I want a post card that looks good and advertises free listings. I need to make sure that this card says in small print that "certain conditions may apply". I want the card to have to be presented in order to get this deal. That this deal is for a limited time only. The companies address is 27410 N Harlow Ave, Ste 118B, Southfield, MI 48991. The office number is 248-555-0143.
Target Market(s)
I am attempting to market to homeowners that want to list there property for sale on the MLS
Industry/Entity Type
Office
Look and feel

```html
<!DOCTYPE html>
<html lang="en">
<head>
<meta charset="utf-8">
<title>Envoy Home Realty – Postcard</title>
<link href="https://fonts.googleapis.com/css2?family=PT+Sans+Narrow:wght@400;700&family=Source+Sans+3:wght@400;600&display=swap" rel="stylesheet">
<style>
  :root {
    --navy: #2b3580;
    --ink: #2a2a2a;
    --grey: #555;
    --red: #c4161c;
    --page: #ececec;
    --card: #ffffff;
    --stamp: #d4d4d6;
    --grass-top: #cfd9c0;
    --grass: #8ea65a;
    --grass-deep: #6f8d3e;
    --key-blue: #2f7fc4;
  }
  * { box-sizing: border-box; margin: 0; padding: 0; }
  html, body { width: 1200px; height: 1196px; overflow: hidden; }
  body { background: var(--page); position: relative; font-family: "Source Sans 3", sans-serif; color: var(--ink); }

  .card { position: absolute; background: var(--card); overflow: hidden; box-shadow: 0 10px 28px rgba(0,0,0,.25); }
  .condensed { font-family: "PT Sans Narrow", sans-serif; }
  .brand-name { font-family: "PT Sans Narrow", sans-serif; font-weight: 700; color: var(--navy); white-space: nowrap; }

  /* Mailing side */
  .card-back { left: 23px; top: 19px; width: 807px; height: 620px;
    background: linear-gradient(120deg, #fff 35%, #f1f1f3 60%, #fff 85%); }
  .card-back .hero-photo { position: absolute; left: 0; top: 46px; width: 215px; height: 300px;
    background: radial-gradient(ellipse at 50% 40%, #d9a08a 0%, #e8d9cf 35%, #c9d3b8 65%, rgba(255,255,255,0) 85%); }
  .card-back .brand-name { position: absolute; left: 210px; top: 98px; font-size: 28px; }
  .card-back .address { position: absolute; left: 211px; top: 137px; font-size: 16px; color: var(--grey); }
  .card-back .headline { position: absolute; left: 200px; top: 172px; font-size: 36px; font-weight: 700; color: var(--navy); }
  .card-back .intro { position: absolute; left: 200px; top: 224px; width: 200px; font-size: 18.5px; line-height: 24px; }
  .card-back .trust { position: absolute; left: 42px; top: 364px; width: 360px; font-size: 18.5px; line-height: 24px; }
  .card-back .offer { position: absolute; left: 42px; top: 416px; font-size: 26px; color: var(--ink); }
  .card-back .offer strong { font-family: "Source Sans 3", sans-serif; font-weight: 600; color: var(--red); font-size: 31px; }
  .card-back .phone { position: absolute; left: 42px; top: 456px; font-size: 46px; font-weight: 700; color: var(--navy); }
  .card-back .stamp-box { position: absolute; left: 629px; top: 38px; width: 141px; height: 141px; background: var(--stamp); }

  /* Offer side */
  .card-front { left: 365px; top: 525px; width: 793px; height: 615px;
    background: linear-gradient(180deg, #ffffff 0%, #f2f4f7 50%, var(--grass-top) 67%, var(--grass) 78%, var(--grass-deep) 100%); }
  .card-front .brand-name { position: absolute; left: 0; right: 0; top: 78px; text-align: center; font-size: 46px; }
  .card-front .family-photo { position: absolute; left: 18px; top: 192px; width: 320px; height: 238px; border-radius: 40% 40% 10% 10%;
    background: radial-gradient(ellipse at 50% 45%, #c99a7e 0%, #e6dcd4 50%, rgba(255,255,255,0) 78%); }
  .card-front .key-tag { position: absolute; left: 307px; top: 150px; width: 230px; height: 265px;
    background: radial-gradient(ellipse at 45% 55%, var(--key-blue) 0%, #5ea2d8 45%, rgba(255,255,255,0) 75%); }
  .card-front .cta-lead { position: absolute; left: 514px; top: 306px; font-size: 24px; color: var(--ink); }
  .card-front .phone { position: absolute; left: 512px; top: 330px; font-size: 46px; font-weight: 700; color: var(--navy); }
  .card-front .deadline { position: absolute; left: 0; right: 0; top: 455px; text-align: center; font-size: 46px; color: #fff; }
  .card-front .fine-print { position: absolute; left: 0; right: 0; top: 512px; text-align: center; font-size: 18px; color: var(--ink); }
  .card-front .address { position: absolute; left: 0; right: 0; top: 536px; text-align: center; font-size: 24px; color: var(--ink); }
</style>
</head>
<body>
  <section class="card card-back">
    <div class="hero-photo" role="img" aria-label="Photo of a hand holding a small model house above a fan of dollar bills"></div>
    <div class="brand-name">Envoy Home Realty, Inc.</div>
    <p class="address condensed">27410 N Harlow Ave, Ste 118B, Southfield, MI 48991</p>
    <h1 class="headline condensed">Buy, Sell or Invest in property</h1>
    <p class="intro">We'll guide you to the best properties and units for sale that will be well-suited to your budget.</p>
    <p class="trust">You can trust you'll receive nothing but the best with Envoy Home Realty</p>
    <p class="offer condensed"><strong>FREE</strong> listings Call Us Now</p>
    <p class="phone condensed">248-555-0143</p>
    <div class="stamp-box"></div>
  </section>

  <section class="card card-front">
    <div class="brand-name">Envoy Home Realty, Inc.</div>
    <div class="family-photo" role="img" aria-label="Photo of a smiling family of four lying together on the grass"></div>
    <div class="key-tag" role="img" aria-label="Illustration of a blue house-shaped key tag reading Free Listings"></div>
    <p class="cta-lead condensed">for more info call us now</p>
    <p class="phone condensed">248-555-0143</p>
    <p class="deadline condensed">This deal is for a limited time only</p>
    <p class="fine-print condensed">*certain conditions may apply</p>
    <p class="address condensed">27410 N Harlow Ave, Ste 118B, Southfield, MI 48991</p>
  </section>
</body>
</html>
```